Please wait to be seated sign A1

We need a sign for our guests on arrival before they get seated:
A1 Size with a 2.2mm bleed
(text)
please wait - someone from our flock will be with you soon.
(must have)
Pink, Simple, Bright and Fun
We are The Velvet Heron and we put on shows so we need it to be creative. Show venue so the use of curtains or stage shows and lots of pink needs to be used. Logo centre up the the top.
Sign 2: Toilet Sign
We want something cute for a toilet directional sign
Female Flamingo and Male Flamingo
(text)
Toilets this way - if there is a cute saying or something cheeky we can do this also
Sign 3:
Platinum Members Only
Sign 4:
Gold Members Only
Sign 5:
Powder Room
Sign 6:
Arrow Sign - See photo for reference
50cm x 18cm with a 2.2mm bleed
Box Office
Sign 7:
Riverside Entry
velvetheronshows.example is the website for reference to who we are fonts and posters we use for our shows. Keep to all pink and cute.
20 - 55
Entertainment

```html
<!DOCTYPE html>
<html lang="en">
<head>
<meta charset="utf-8">
<title>Box Office – Arrow Sign</title>
<link rel="stylesheet" href="https://fonts.googleapis.com/css2?family=Barlow+Condensed:wght@700&display=swap">
<style>
  :root {
    --blush: #fde9fc;
    --magenta: #f52af0;
    --brush-hot: #f0339a;
    --brush-pink: #f25ad9;
    --brush-soft: #f8a6ec;
  }
  html, body {
    margin: 0;
    padding: 0;
    overflow: hidden;
  }
  .sign {
    position: relative;
    width: 1200px;
    height: 366px;
    background: var(--blush);
    overflow: hidden;
  }
  .brush-strokes {
    position: absolute;
    left: 0;
    top: 0;
    width: 250px;
    height: 366px;
    background:
      radial-gradient(ellipse 160px 120px at 40px 40px, var(--brush-hot) 0%, rgba(240, 51, 154, 0) 100%),
      radial-gradient(ellipse 150px 170px at 10px 190px, var(--brush-pink) 0%, rgba(242, 90, 217, 0) 100%),
      radial-gradient(ellipse 130px 120px at 20px 320px, var(--brush-soft) 0%, rgba(248, 166, 236, 0) 100%),
      linear-gradient(90deg, rgba(242, 90, 217, 0.55) 0%, rgba(248, 166, 236, 0) 100%);
  }
  .sign-title {
    position: absolute;
    left: 180px;
    top: 112px;
    margin: 0;
    font-family: "Barlow Condensed", "Arial Narrow", sans-serif;
    font-weight: 700;
    font-size: 152px;
    line-height: 1;
    letter-spacing: 1px;
    color: var(--magenta);
    white-space: nowrap;
  }
</style>
</head>
<body>
  <main class="sign">
    <div class="brush-strokes" role="img" aria-label="Pink watercolour brush strokes sweeping in from the left edge"></div>
    <h1 class="sign-title">Box Office</h1>
  </main>
</body>
</html>
```